Need a powerful, eye-catching book cover design for a Public Relations book for Lawyers.

We need a beautiful, elegant, and professional cover for a public relations book. We’ll be selling this both to (1) creative, experienced legal marketers, and (2) conservative lawyers. It must grab their attention visually, and have a bold, easy to read headline. The cover image may wrap around to the back cover.SIZE: 6 x 9” 100 pagesTITLE: The Ultimate Public Relations Handbook for LawyersSUBHEAD: Make millions using media and the InternetCO-AUTHORSRoss Fishman, JDJohn HellermanInclude a CALLOUT quote: “The definitive PR book. Simple and powerful.” – Tad Lurvey, SkaddenGRAPHICS:You may use one of the attached photos, crop or flip them however you’d like, or use something else entirely. DESCRIPTION for the back cover:Why do some law firms have the best reputations or command the highest hourly rates? Why are some the go-to firms or thought leaders in particular specialties? Why are your competitors in the media more than you? Two words: Public relations. The co-authors are known worldwide as leaders in public relations, legal marketing, and branding. Neil Stamford is called, “A PR Guru.” Bar Ledger magazine wrote ““Many people consider Dale Warbeck to be the nation’s foremost expert on law firm marketing.”Tad Lurvey built Brommick into the first firm to generate $1 billion in revenue. Yvonne Pelstrup is the nation’s go-to lawyer for women’s issues. Your home town’s top PI lawyer gets the first look at the biggest cases. Why? Strategic, intentional, effective PR. Are you tired of toiling in anonymity? Want to earn the attention of reporters and editors who can build your credentials and reputation for expertise? Wouldn’t it be nice to have more clients begging you to represent them because they heard you were the best in town? That is what public relations is designed to do. Want to get more respect, earn more clients, and charge higher rates? Get known as a thought leader in a specialty practice or industry? Public relations could be your most-important marketing tool. And this book will teach you precisely how. Ready to catapult your practice to new heights? Take a deep breath and dive in….

Target Market(s)

1. Creative marketing professionals
2. Conservative 40-year-old lawyers

Industry/Entity Type

Legal

Font styles to use
Serif

Requirements
Must have
• Want a simple, bold, eye catching design conveying professionalism and quality. This is a practical, how-to book. We need a simple design and strong headline that will work well at a small thumbnail size on Zelbora.
Nice to have
• Perhaps the microphone could wrap around the cover? A tight crop of a microphone that creates an abstract could work. Let's create something memorable.

```html
<!DOCTYPE html>
<html lang="en">
<head>
<meta charset="utf-8">
<title>The Complete Press Outreach Manual for Attorneys — Cover</title>
<link rel="stylesheet" href="https://fonts.googleapis.com/css2?family=Josefin+Sans:wght@400;600;700&family=Lora:ital,wght@1,400&display=swap">
<style>
  :root {
    --page-bg: #f3f3f3;
    --navy-deep: #0d1533;
    --navy-mid: #1b2a5e;
    --navy-light: #2c3f80;
    --ink-light: #ffffff;
    --ink-soft: #d9deee;
    --silver: #d3d7e0;
    --silver-soft: rgba(190, 197, 214, 0.35);
  }
  * { box-sizing: border-box; margin: 0; padding: 0; }
  html, body {
    width: 1200px; height: 800px; overflow: hidden;
    background: var(--page-bg);
  }
  .spread {
    position: absolute; left: 148px; top: 70px;
    display: flex; gap: 24px;
  }
  .cover {
    position: relative; width: 440px; height: 660px;
    background: radial-gradient(ellipse at 35% 45%, var(--navy-light) 0%, var(--navy-mid) 45%, var(--navy-deep) 100%);
    color: var(--ink-light);
    overflow: hidden;
  }
  /* Back cover */
  .back-copy {
    position: absolute; left: 34px; top: 44px; right: 34px;
    font-family: "Josefin Sans", sans-serif;
    font-size: 8.6px; line-height: 1.55; letter-spacing: 0.09em;
    text-transform: uppercase; color: var(--ink-soft);
  }
  .back-copy p { margin-bottom: 9px; }
  /* Front cover */
  .callout {
    position: absolute; top: 28px; left: 20px; right: 20px; text-align: center;
  }
  .callout-quote {
    font-family: "Lora", serif; font-style: italic;
    font-size: 15px; color: var(--ink-light);
  }
  .callout-source {
    margin-top: 8px;
    font-family: "Josefin Sans", sans-serif; font-size: 11px;
    letter-spacing: 0.1em; text-transform: uppercase; color: var(--ink-soft);
    padding-left: 150px;
  }
  .mic-art {
    position: absolute; left: 0; top: 150px; width: 250px; height: 320px;
    background:
      radial-gradient(ellipse 70px 55px at 180px 70px, var(--silver) 0%, var(--silver-soft) 55%, transparent 100%),
      radial-gradient(ellipse 70px 40px at 60px 125px, var(--silver-soft) 0%, transparent 100%),
      radial-gradient(ellipse 55px 50px at 150px 195px, var(--silver) 0%, var(--silver-soft) 55%, transparent 100%),
      radial-gradient(ellipse 50px 40px at 90px 280px, var(--silver) 0%, var(--silver-soft) 55%, transparent 100%);
  }
  .title {
    position: absolute; right: 24px; top: 240px; width: 200px;
    font-family: "Josefin Sans", sans-serif; font-weight: 700;
    font-size: 24px; line-height: 1.15; text-align: right;
    color: var(--ink-light);
  }
  .subhead {
    position: absolute; right: 22px; top: 412px; width: 200px;
    font-family: "Josefin Sans", sans-serif; font-size: 12px;
    line-height: 1.45; letter-spacing: 0.08em; text-transform: uppercase;
    text-align: right; color: var(--ink-soft);
  }
  .authors {
    position: absolute; left: 0; right: 0; bottom: 52px; text-align: center;
    font-family: "Josefin Sans", sans-serif; font-size: 11px;
    letter-spacing: 0.12em; text-transform: uppercase; color: var(--ink-soft);
    padding-left: 40px;
  }
</style>
</head>
<body>
  <main class="spread">
    <section class="cover cover-back">
      <div class="back-copy">
        <p>Why do some law firms have the best reputations or command the highest hourly rates?</p>
        <p>Why are some the go-to firms or thought leaders in particular specialties?</p>
        <p>Why are your competitors in the media more than you?</p>
        <p>Two words: Public relations.</p>
        <p>The co-authors are known worldwide as leaders in public relations, legal marketing, and branding.</p>
        <p>Neil Stamford is called, “A PR Guru.” Bar Ledger magazine wrote “Many people consider Dale Warbeck to be the nation’s foremost expert on law firm marketing.”</p>
        <p>Tad Lurvey built Brommick into the first firm to generate $1 billion in revenue.</p>
        <p>Yvonne Pelstrup is the nation’s go-to lawyer for women’s issues.</p>
        <p>Your home town’s top PI lawyer gets the first look at the biggest cases. Why? Strategic, intentional, effective PR. Are you tired of toiling in anonymity? Want to earn the attention of reporters and editors who can build your credentials and reputation for expertise? Wouldn’t it be nice to have more clients begging you to represent them because they heard you were the best in town? That is what public relations is designed to do. Want to get more respect, earn more clients, and charge higher rates? Get known as a thought leader in a specialty practice or industry? Public relations could be your most-important marketing tool. And this book will teach you precisely how. Ready to catapult your practice to new heights? Take a deep breath and dive in…</p>
      </div>
    </section>

    <section class="cover cover-front">
      <div class="callout">
        <p class="callout-quote">“The definitive PR book. Simple and powerful.”</p>
        <p class="callout-source">- Tad Lurvey, Brommick -</p>
      </div>
      <div class="mic-art" role="img" aria-label="Close crop of several silver microphones angled in from the left"></div>
      <h1 class="title">The Complete Press Outreach Manual for Attorneys</h1>
      <p class="subhead">Make millions using<br>media and the Internet</p>
      <p class="authors">Dale Warbeck, Neil Stamford</p>
    </section>
  </main>
</body>
</html>
```